3 Bright Fun Kids Book Covers

I am launching a kids book series called Merry Tiny Thinkers. These are activity books designed for kids from 3 - 5. They cover all brain training and hand training elements - scissor cutting, using pencils - as a great support for kindergarten activities. I am looking for 3 bright, happy and engaging book covers for the first three books in the series: Book 1: Scissor Skills Activity Book for Kids Ages 3 - 5: Cutting Practice and Fine Motor Activities for Preschool and Kindergarten | Merry Tiny Thinkers, Book 2: Pencil Control Activity Book for Kids Ages 3–5: Pre-Writing Tracing Lines and Handwriting Readiness Workbook | Merry Tiny Thinkers, Book 3: Tracing Letters Activity Book for Kids Ages 3 - 5: Alphabet Tracing Workbook for Preschool and Kindergarten | Merry Tiny Thinkers.

They need to look like they all come from the same family. The category works well if each book has a different primary colour. The three covers will be featured on the back of each book to signal that these are part of a series. Along with the brand. The series will grow to 10 books over time - so this is the foundation for the future.

Covers for competitive scissors activity books clearly show the scissors cutting around the image. The drawings I have included are actual content and show the scissors - these can be coloured to appeal on the cover. Competitive covers for pencil holding books show the activity is about tracing along an activity line - that starts with simple straight lines and builds to more complex images. I have uploaded the content for this book so you can see it. The books on letter tracing display the pencil direction drawings and traceable letter elements - I have uploaded photos of the type of pages.

The competitive cover research for the scissors books which are similar to other kids activity books I have attached
The size of each book is 8.5 x 11 inch
I have a logo for Merry Tiny Thinkers - Square sized that I can provide to the winning designs to add. In the uploaded copy of the scissors book you will see the logo.

I am looking for a family of the three cover designs please.

```html
<!DOCTYPE html>
<html lang="en">
<head>
<meta charset="utf-8">
<title>Scissor Skills Activity Book – Merry Tiny Thinkers</title>
<link href="https://fonts.googleapis.com/css2?family=Titan+One&family=Itim&display=swap" rel="stylesheet">
<style>
  :root {
    --page-bg: #4a4a4a;
    --sun-top: #fdd333;
    --sun-mid: #fca12c;
    --sun-bottom: #fb7d22;
    --paper: #ffffff;
    --sticker-edge: #f1f1f1;
    --ink: #1a1a1a;
    --red: #d11f2e;
    --scissor-red: #e8452c;
    --blade: #b9bdc3;
    --green: #2aa43c;
    --blue: #0f4fae;
    --gold: #f6a30f;
    --mint: #2fb86a;
    --sky: #5ec8f0;
    --yellow: #fbbf15;
  }
  * { margin: 0; padding: 0; box-sizing: border-box; }
  html, body { width: 1200px; height: 2249px; overflow: hidden; background: var(--page-bg); }
  .stage { position: relative; width: 1200px; height: 2249px; }
  .cover {
    position: absolute; left: 0; top: 348px;
    width: 1046px; height: 1353px;
    transform: scale(1.1472); transform-origin: 0 0;
    background: linear-gradient(180deg, var(--sun-top) 0%, var(--sun-mid) 35%, var(--sun-bottom) 70%, var(--sun-bottom) 100%);
    overflow: hidden;
  }
  .cover-shapes { position: absolute; inset: 0; width: 1046px; height: 1353px; }

  .sticker {
    position: absolute; border-radius: 46%;
    background: var(--paper);
    box-shadow: 0 3px 8px rgba(0,0,0,0.12);
  }
  .sticker::before {
    content: ""; position: absolute; inset: 7px; border-radius: 46%;
    border: 1.5px dashed rgba(26,26,26,0.45);
  }
  .sticker::after {
    content: ""; position: absolute; inset: 18px; border-radius: 44%;
    background: var(--fill);
  }
  .art-helicopter { left: 66px; top: 37px; width: 290px; height: 225px; --fill: radial-gradient(circle at 55% 45%, #e46cd6 0%, #f4a6ec 55%, var(--sticker-edge) 100%); }
  .art-dolphin { left: 51px; top: 612px; width: 275px; height: 305px; --fill: radial-gradient(circle, #2f9bd0 0%, #7cc6e8 55%, var(--sticker-edge) 100%); }
  .art-snail { left: 726px; top: 687px; width: 270px; height: 235px; --fill: radial-gradient(circle at 60% 50%, #e07a28 0%, #d2b66a 55%, var(--sticker-edge) 100%); }
  .art-caterpillar { left: 21px; top: 947px; width: 330px; height: 290px; --fill: radial-gradient(circle, #a9e047 0%, #cdee8f 55%, var(--sticker-edge) 100%); }
  .art-octopus { left: 711px; top: 1007px; width: 300px; height: 285px; --fill: radial-gradient(circle, #ee7ee0 0%, #f4b3ec 55%, var(--sticker-edge) 100%); }

  .age-badge {
    position: absolute; left: 735px; top: 86px; width: 196px; height: 196px;
    border-radius: 50%; background: var(--red);
    display: flex; flex-direction: column; align-items: center; justify-content: center;
    font-family: "Titan One", sans-serif; line-height: 1;
  }
  .age-badge::after {
    content: ""; position: absolute; inset: 4px; border-radius: 50%;
    border: 2px dashed var(--ink);
  }
  .age-badge .for-kids { color: var(--paper); font-size: 24px; }
  .age-badge .ages { color: var(--sky); font-size: 44px; margin-top: 4px; }
  .age-badge .range { color: var(--yellow); font-size: 38px; margin-top: 2px; }

  .title { font-weight: normal; }
  .title-line {
    position: absolute; display: block; white-space: nowrap;
    font-family: "Titan One", sans-serif; line-height: 1;
  }
  .title-line-1 { top: 300px; left: 291px; font-size: 112px; color: var(--gold); text-shadow: 5px 5px 0 var(--ink); }
  .title-line-2 { top: 400px; left: 0; width: 1056px; text-align: center; font-size: 172px; text-shadow: 7px 7px 0 var(--ink); }
  .c-red { color: var(--red); } .c-green { color: var(--green); } .c-blue { color: var(--blue); }
  .c-gold { color: var(--gold); } .c-mint { color: var(--mint); }

  .series-pill {
    position: absolute; left: 324px; top: 575px; width: 397px; height: 67px;
    background: var(--red); border-radius: 34px;
    display: flex; align-items: center; justify-content: center;
    font-family: "Titan One", sans-serif; font-size: 36px; color: var(--paper);
    letter-spacing: 1px;
  }
  .series-pill::after {
    content: ""; position: absolute; inset: 5px; border-radius: 30px;
    border: 2px dashed rgba(255,255,255,0.75);
  }
  .subtitle {
    position: absolute; left: 323px; top: 684px; width: 400px; text-align: center;
    font-family: "Itim", sans-serif; font-size: 30px; line-height: 1.12; color: var(--ink);
  }
  .brand {
    position: absolute; left: 384px; top: 880px; width: 322px; text-align: center;
    font-family: "Titan One", sans-serif; font-size: 58px; line-height: 1.05; color: var(--blue);
  }
</style>
</head>
<body>
<main class="stage">
  <section class="cover" aria-label="Scissor Skills Activity Book cover">
    <svg class="cover-shapes" viewBox="0 0 1046 1353" aria-hidden="true">
      <defs>
        <symbol id="scissors-icon" viewBox="0 0 100 100">
          <polygon points="40,58 94,14 98,20 48,66" fill="#b9bdc3" stroke="#8e9399" stroke-width="2"/>
          <polygon points="44,66 96,34 98,42 50,74" fill="#b9bdc3" stroke="#8e9399" stroke-width="2"/>
          <circle cx="26" cy="54" r="15" fill="none" stroke="#e8452c" stroke-width="9"/>
          <circle cx="40" cy="82" r="13" fill="none" stroke="#c0392b" stroke-width="9"/>
        </symbol>
      </defs>
      <path class="cut-line" d="M466 0 C470 60 495 100 501 140" fill="none" stroke="#1a1a1a" stroke-width="3" stroke-dasharray="12 9"/>
      <path class="cut-line" d="M0 437 C40 460 90 478 141 482" fill="none" stroke="#1a1a1a" stroke-width="3" stroke-dasharray="12 9"/>
      <path class="cut-line" d="M896 572 C950 555 1000 545 1046 545" fill="none" stroke="#1a1a1a" stroke-width="3" stroke-dasharray="12 9"/>
      <path class="paper-panel" d="M150 240 C250 180 380 200 470 250 C560 200 650 130 760 110 L885 300 C900 450 870 550 890 650 C910 800 960 900 950 1050 C940 1200 870 1280 760 1270 C600 1250 450 1160 320 1180 C200 1200 120 1150 120 1050 C120 930 150 850 170 700 C190 560 110 450 120 350 Z" fill="#ffffff"/>
      <path class="paper-cut-guide" transform="translate(21 27) scale(0.96)" d="M150 240 C250 180 380 200 470 250 C560 200 650 130 760 110 L885 300 C900 450 870 550 890 650 C910 800 960 900 950 1050 C940 1200 870 1280 760 1270 C600 1250 450 1160 320 1180 C200 1200 120 1150 120 1050 C120 930 150 850 170 700 C190 560 110 450 120 350 Z" fill="none" stroke="#1a1a1a" stroke-width="3" stroke-dasharray="14 10"/>
      <use class="scissors-main" href="#scissors-icon" x="466" y="110" width="230" height="200"/>
      <use class="scissors-small" href="#scissors-icon" x="181" y="302" width="115" height="115"/>
      <use class="scissors-small" href="#scissors-icon" x="40" y="430" width="60" height="60"/>
      <use class="scissors-small" href="#scissors-icon" x="862" y="335" width="52" height="52"/>
      <use class="scissors-small" href="#scissors-icon" x="935" y="530" width="60" height="60"/>
    </svg>

    <div class="sticker art-helicopter" role="img" aria-label="Cut-out sticker of a smiling pink cartoon helicopter"></div>

    <div class="age-badge">
      <span class="for-kids">FOR KIDS</span>
      <span class="ages">AGES</span>
      <span class="range">3 TO 5</span>
    </div>

    <h1 class="title">
      <span class="title-line title-line-1">SCISSOR</span>
      <span class="title-line title-line-2"><span class="c-red">S</span><span class="c-green">K</span><span class="c-blue">I</span><span class="c-gold">L</span><span class="c-red">L</span><span class="c-mint">S</span></span>
    </h1>

    <div class="series-pill">ACTIVITY BOOK</div>

    <p class="subtitle">Cutting Practice<br>and Fine Motor Activities<br>for Preschool<br>and Kindergarten</p>

    <div class="sticker art-dolphin" role="img" aria-label="Cut-out sticker of a jumping blue cartoon dolphin"></div>
    <div class="sticker art-snail" role="img" aria-label="Cut-out sticker of a cartoon snail with an orange shell"></div>
    <div class="sticker art-caterpillar" role="img" aria-label="Cut-out sticker of a green cartoon caterpillar wearing boots"></div>
    <div class="sticker art-octopus" role="img" aria-label="Cut-out sticker of a pink cartoon octopus"></div>

    <p class="brand">Merry<br>Tiny<br>Thinkers</p>
  </section>
</main>
</body>
</html>
```